Banner 34"x81"

This is for a Pull Up Banner
I am supplying a sample of my logo and some of my art work for you to incorporate into an upright banner.
Please business name:LuellaRo OpenHarbor Psychotherapy
phone number: 583-214-9067 NOT THE ONE ON THE BUSINESS CARD

```html
<!DOCTYPE html>
<html lang="en">
<head>
<meta charset="utf-8">
<title>OpenHarbor Psychotherapy – Pull Up Banner</title>
<link rel="stylesheet" href="https://fonts.googleapis.com/css2?family=Big+Shoulders+Inline+Display:wght@700&family=Open+Sans:wght@400;700&family=Lexend:wght@700&family=Noto+Sans+SC:wght@400&display=swap">
<style>
  :root {
    --sky: #00b0ec;
    --steel: #4a7a90;
    --night: #000000;
    --panel: #0e111c;
    --white: #ffffff;
    --ice-blue: #5bb4e6;
    --brand-blue: #1f57a8;
    --butter: #fcec7e;
    --ink: #121212;
  }
  * { margin: 0; padding: 0; box-sizing: border-box; }
  html, body { width: 1200px; height: 2859px; overflow: hidden; }
  body {
    position: relative;
    background: linear-gradient(180deg, var(--sky) 0px, #0290c0 170px, var(--steel) 520px, #2a3a44 900px, #0a0a0c 1300px, var(--night) 1500px);
    font-family: "Open Sans", sans-serif;
    color: var(--white);
  }
  .abs { position: absolute; }
  .practice-name {
    top: 190px; left: 0; width: 1200px; text-align: center;
    font-family: "Big Shoulders Inline Display", sans-serif;
    font-weight: 700; font-size: 236px; line-height: 1; letter-spacing: 4px;
  }
  .practice-type {
    top: 422px; left: 0; width: 1176px; text-align: center;
    font-weight: 700; font-size: 92px; line-height: 1;
  }
  .info-panel { top: 600px; left: 105px; width: 983px; height: 2137px; background: var(--panel); }
  .feature-frame { top: 664px; left: 198px; width: 790px; height: 974px; border: 3px solid var(--white); }
  .portrait {
    top: 592px; left: 572px; width: 532px; height: 532px; border-radius: 50%;
    background: radial-gradient(circle at 50% 40%, #6a4a44 0%, #3a2420 45%, #1d1412 70%, #2b56b6 88%, #2f5ec4 100%);
  }
  .tagline-cn {
    top: 896px; left: 283px; width: 156px; height: 650px;
    writing-mode: vertical-rl; text-orientation: upright;
    font-family: "Noto Sans SC", sans-serif; font-size: 148px; line-height: 156px;
    letter-spacing: 10px; color: var(--ice-blue);
  }
  .brand-mark {
    top: 1220px; left: 521px; width: 369px; height: 301px; background: var(--brand-blue);
    display: flex; align-items: center; justify-content: center;
    font-weight: 700; font-size: 66px; color: var(--white);
  }
  .therapist-name {
    top: 1718px; left: 105px; width: 983px; text-align: center;
    font-weight: 700; font-size: 156px; line-height: 1; letter-spacing: -2px;
  }
  .email { top: 1904px; left: 105px; width: 935px; text-align: center; font-size: 47px; }
  .phone-band {
    top: 2026px; left: 102px; width: 983px; height: 157px; background: var(--butter);
    display: flex; align-items: center; justify-content: center;
    font-family: "Lexend", sans-serif; font-weight: 700; font-size: 120px; color: var(--ink);
    letter-spacing: 5px;
  }
  .social-dot { left: 526px; width: 92px; height: 92px; border-radius: 50%; background: var(--butter); }
  .social-dot.facebook { top: 2271px; }
  .social-dot.twitter { top: 2487px; }
  .handle { left: 105px; width: 935px; text-align: center; font-size: 47px; }
  .handle.facebook { top: 2384px; }
  .handle.twitter { top: 2606px; }
  .footer-band { top: 2737px; left: 0; width: 1200px; height: 122px; background: var(--butter); }
</style>
</head>
<body>
  <div class="abs practice-name">OPENHARBOR</div>
  <div class="abs practice-type">Psychotherapy</div>

  <div class="abs info-panel"></div>
  <div class="abs feature-frame"></div>
  <div class="abs portrait" role="img" aria-label="Portrait photo of the therapist seated in a leather chair"></div>
  <div class="abs tagline-cn" lang="zh">开放港湾</div>
  <div class="abs brand-mark">LuellaRo</div>

  <div class="abs therapist-name">LuellaRo</div>
  <div class="abs email">LuellaOpenHarbor@harbormail.com</div>
  <div class="abs phone-band">583-214-9067</div>

  <div class="abs social-dot facebook"></div>
  <div class="abs handle facebook">@LuellaOpenHarbour</div>
  <div class="abs social-dot twitter"></div>
  <div class="abs handle twitter">@LuellaHarbor</div>

  <div class="abs footer-band"></div>
</body>
</html>
```